Business Cards for a law firm

Business cards for our law firm. Use our silhoette logo and OAK COUNSEL - check our website (www.oakcounsel.com)

Contact Information for Business Card

our silhouette logo, OAK COUNSEL, 800-555-0147, Dariel Montague, dariel@oakcounsel.com

Requirements
Must have
• our silhouette logo, OAK COUNSEL, 800-555-0147, Dariel Montague, dariel@oakcounsel.com

```html
<!DOCTYPE html>
<html lang="en">
<head>
<meta charset="utf-8">
<title>Oak Counsel — Business Card</title>
<link href="https://fonts.googleapis.com/css2?family=Cinzel:wght@600&family=Montserrat:wght@500;600;700&display=swap" rel="stylesheet">
<style>
  :root {
    --page-bg: #eceef2;
    --card-blue: #1c3f80;
    --ink-light: #ffffff;
  }
  * { box-sizing: border-box; margin: 0; padding: 0; }
  html, body {
    width: 1200px;
    height: 1111px;
    overflow: hidden;
    background: var(--page-bg);
  }
  .canvas {
    position: relative;
    width: 1200px;
    height: 1111px;
  }
  .business-card {
    position: absolute;
    left: 135px;
    top: 285px;
    width: 930px;
    height: 540px;
    background: var(--card-blue);
    border-radius: 34px;
    color: var(--ink-light);
    font-family: "Montserrat", sans-serif;
  }
  .brand {
    position: absolute;
    left: 34px;
    top: 58px;
    display: flex;
    align-items: center;
    gap: 26px;
  }
  .brand-mark {
    width: 70px;
    height: 70px;
    background: var(--ink-light);
  }
  .brand-name {
    font-family: "Cinzel", serif;
    font-weight: 600;
    font-size: 76px;
    letter-spacing: 3px;
    line-height: 1;
    color: var(--ink-light);
  }
  .holder {
    position: absolute;
    left: 130px;
    top: 212px;
  }
  .holder-name {
    font-weight: 700;
    font-size: 25px;
    margin-bottom: 18px;
  }
  .holder-role {
    font-weight: 600;
    font-size: 25px;
  }
  .contact-row {
    position: absolute;
    left: 130px;
    top: 440px;
    display: flex;
    gap: 80px;
    font-weight: 500;
    font-size: 25px;
  }
  .contact-item {
    display: flex;
    align-items: center;
    gap: 16px;
  }
  .contact-icon {
    width: 26px;
    height: 26px;
    flex: none;
  }
</style>
</head>
<body>
  <main class="canvas">
    <section class="business-card">
      <div class="brand">
        <div class="brand-mark"></div>
        <h1 class="brand-name">OAK COUNSEL</h1>
      </div>

      <div class="holder">
        <p class="holder-name">Dariel Montague</p>
        <p class="holder-role">Attorney | Reserve Dep. Sheriff</p>
      </div>

      <div class="contact-row">
        <div class="contact-item">
          <svg class="contact-icon" viewBox="0 0 24 24" aria-hidden="true">
            <path fill="#ffffff" d="M6.6 10.8a15.1 15.1 0 0 0 6.6 6.6l2.2-2.2a1 1 0 0 1 1-.25 11.4 11.4 0 0 0 3.6.57 1 1 0 0 1 1 1V20a1 1 0 0 1-1 1A17 17 0 0 1 3 4a1 1 0 0 1 1-1h3.5a1 1 0 0 1 1 1c0 1.25.2 2.45.57 3.57a1 1 0 0 1-.25 1z"/>
          </svg>
          <span class="contact-text">800-555-0147</span>
        </div>
        <div class="contact-item">
          <svg class="contact-icon" viewBox="0 0 24 24" aria-hidden="true">
            <circle cx="12" cy="12" r="10" fill="#ffffff"/>
            <path d="M2 12h20M12 2c3 3 3 17 0 20M12 2c-3 3-3 17 0 20" fill="none" stroke="#1c3f80" stroke-width="1.6"/>
          </svg>
          <span class="contact-text">dariel@oakcounsel.com</span>
        </div>
      </div>
    </section>
  </main>
</body>
</html>
```